Brightmoor Auto Care 4x9 Rack Card

Design a 4" wide by 9" tall rack card printed front and back using the copy, logo and images uploaded below. I am also uploading a current flyer so you can see the typestyles we use. I will get the exact name of the font for you ASAP. Also will be uploading some before and after pictures for the back of the rack card

Target Market(s)

Affluent consumers who need their car cleaned and detailed in a meticulous fashion

Requirements
Must have
• Under the logo, put the words...... Premium Steam Detailing & Ceramic Coating.........also put ther following wording on the front side: Get Steamed! We use steam to clean your vehicle helping save millions of gallons of water and protecting our rivers, streams and lakes from runoff.
Nice to have
• a screened back background of hexagons might be nice

```html
<!DOCTYPE html>
<html lang="en">
<head>
<meta charset="utf-8">
<title>Brightmoor Auto Care – Rack Card Front &amp; Back</title>
<link href="https://fonts.googleapis.com/css2?family=Oswald:wght@500;600&family=Arimo:ital,wght@0,400;1,400&family=Montserrat:wght@700;800&family=Cabin:wght@400&family=Great+Vibes&display=swap" rel="stylesheet">
<style>
  :root{
    --bg:#676966;
    --blue:#4a84c6;
    --green:#6aad52;
    --white:#ffffff;
    --grey-band:#e4e5e6;
    --photo-dark:#3d4248;
    --photo-mid:#9aa3ab;
  }
  html,body{margin:0;padding:0;width:1200px;height:1200px;overflow:hidden;background:var(--bg);}
  .stage{position:absolute;left:0;top:0;width:1932px;height:1932px;transform:scale(0.62112);transform-origin:0 0;}
  .card{position:absolute;top:260px;width:622px;height:1398px;background:var(--white);overflow:hidden;}
  .card--front{left:287px;}
  .card--back{left:1022px;background:var(--blue);}
  .shapes{position:absolute;left:0;top:0;width:622px;height:1398px;}
  .abs{position:absolute;margin:0;}

  /* front */
  .brand-mark{left:223px;top:470px;width:80px;height:80px;border-radius:50%;background:var(--blue);}
  .brand-name{left:0;width:530px;text-align:center;font-family:'Oswald',sans-serif;font-weight:600;color:var(--green);line-height:1;}
  .brand-name--top{top:580px;font-size:62px;letter-spacing:6px;}
  .brand-name--bottom{top:648px;font-size:40px;letter-spacing:22px;}
  .tagline{left:0;width:532px;top:700px;text-align:center;font-family:'Oswald',sans-serif;font-weight:500;font-size:20px;color:var(--green);letter-spacing:.3px;}
  .intro{left:60px;width:410px;top:740px;text-align:center;font-family:'Arimo',sans-serif;color:var(--blue);}
  .intro__head{font-style:italic;font-size:23px;margin:0 0 4px;}
  .intro__body{font-size:20.5px;line-height:27px;margin:0;letter-spacing:.3px;}
  .locations{left:92px;top:958px;width:360px;font-family:'Arimo',sans-serif;color:var(--white);font-size:21.5px;line-height:28px;letter-spacing:-.3px;}
  .location{position:relative;padding-left:32px;margin-bottom:14px;}
  .location svg{position:absolute;left:0;top:4px;}
  .locations__rule{position:absolute;left:10px;top:28px;width:1.5px;height:236px;background:var(--white);}
  .contact{left:57px;top:1200px;font-family:'Arimo',sans-serif;color:var(--white);}
  .contact__lead{font-style:italic;text-decoration:underline;font-size:24px;margin:0 0 6px;}
  .contact__line{font-family:'Montserrat',sans-serif;font-weight:700;font-size:27px;line-height:34.5px;margin:0;padding-left:4px;}
  .contact__icon{display:inline-block;vertical-align:-5px;margin-right:10px;}

  /* back */
  .tag{position:absolute;background:var(--blue);color:var(--white);font-family:'Montserrat',sans-serif;font-weight:700;font-size:16px;letter-spacing:2px;text-align:center;}
  .tag--v{writing-mode:vertical-rl;transform:rotate(180deg);display:flex;align-items:center;justify-content:center;}
  .prices{left:0;width:606px;top:540px;text-align:center;font-family:'Cabin',sans-serif;color:var(--white);font-size:28px;line-height:35px;}
  .price{margin:0 0 33px;}
  .slogan{left:0;width:606px;top:985px;text-align:center;color:var(--white);}
  .slogan__script{font-family:'Great Vibes',cursive;font-size:48px;line-height:48px;margin:0;}
  .slogan__bold{font-family:'Montserrat',sans-serif;font-weight:800;font-size:36px;margin:0;line-height:44px;}
  .cta{left:0;width:606px;top:1163px;text-align:center;color:var(--white);font-family:'Arimo',sans-serif;}
  .cta__note{font-style:italic;font-size:29px;line-height:38px;margin:0;}
  .cta__phone{font-family:'Montserrat',sans-serif;font-weight:800;font-size:60px;line-height:68px;margin:8px 0 0;}
  .cta__web{font-size:34px;line-height:36px;margin:0;}
</style>
</head>
<body>
<div class="stage">

  <!-- FRONT -->
  <section class="card card--front">
    <svg class="shapes" viewBox="0 0 622 1398">
      <defs>
        <linearGradient id="gradTopPhoto" x1="0" y1="0" x2="1" y2="1">
          <stop offset="0" stop-color="#5d6670"/><stop offset=".5" stop-color="#a9b1b8"/><stop offset="1" stop-color="#2e3338"/>
        </linearGradient>
        <linearGradient id="gradSidePhoto" x1="0" y1="0" x2="1" y2="1">
          <stop offset="0" stop-color="#1b1b1b"/><stop offset=".5" stop-color="#b9a78e"/><stop offset="1" stop-color="#3a3f46"/>
        </linearGradient>
      </defs>
      <polygon role="img" aria-label="Detailer hand-polishing the hood of a silver sports car, shown in a honeycomb collage" fill="url(#gradTopPhoto)"
        points="0,65 100,65 135,0 455,0 495,65 525,65 562,128 525,190 562,250 525,315 562,380 525,445 455,445 418,510 340,510 300,445 100,445 0,445"/>
      <polygon fill="var(--green)" points="0,780 80,920 0,1060"/>
      <polygon fill="var(--blue)" points="93,928 403,928 553,1190 443,1398 45,1398 0,1320 0,1090"/>
      <polygon fill="var(--green)" points="462,1398 560,1212 622,1195 622,1398"/>
      <polygon fill="var(--green)" points="0,1330 38,1398 0,1398"/>
      <polygon role="img" aria-label="Technician steam-cleaning the front grille of a luxury car" fill="url(#gradSidePhoto)"
        points="622,655 622,1190 558,1190 408,928 500,790"/>
    </svg>

    <div class="abs brand-mark"></div>
    <p class="abs brand-name brand-name--top">BRIGHTMOOR</p>
    <p class="abs brand-name brand-name--bottom">AUTO CARE</p>
    <p class="abs tagline">PREMIUM STEAM DETAILING &amp; CERAMIC COATING</p>

    <div class="abs intro">
      <p class="intro__head">GET STEAMED!</p>
      <p class="intro__body">We use steam to clean your<br>vehicle helping save millions of<br>gallons of water &amp; protecting our<br>rivers, &nbsp;streams &amp;<br>lakes from runoff.</p>
    </div>

    <div class="abs locations">
      <div class="locations__rule"></div>
      <div class="location">
        <svg width="20" height="22" viewBox="0 0 20 22"><path d="M10 1a7 7 0 0 0-7 7c0 5 7 13 7 13s7-8 7-13a7 7 0 0 0-7-7z" fill="none" stroke="#fff" stroke-width="2.4"/><circle cx="10" cy="8" r="2.6" fill="#fff"/></svg>
        1450 Larkspur Avenue @<br>The Larkspur Commons<br>Fairhaven
      </div>
      <div class="location">
        <svg width="20" height="22" viewBox="0 0 20 22"><path d="M10 1a7 7 0 0 0-7 7c0 5 7 13 7 13s7-8 7-13a7 7 0 0 0-7-7z" fill="none" stroke="#fff" stroke-width="2.4"/><circle cx="10" cy="8" r="2.6" fill="#fff"/></svg>
        52 Aspenglow Lane<br>Ridgeview Village
      </div>
      <div class="location">
        <svg width="20" height="22" viewBox="0 0 20 22"><path d="M10 1a7 7 0 0 0-7 7c0 5 7 13 7 13s7-8 7-13a7 7 0 0 0-7-7z" fill="none" stroke="#fff" stroke-width="2.4"/><circle cx="10" cy="8" r="2.6" fill="#fff"/></svg>
        318 Crestline Rd #204<br>Pinefield
      </div>
    </div>

    <div class="abs contact">
      <p class="contact__lead">Call for information &amp; scheduling:</p>
      <p class="contact__line">Fairhaven &nbsp;(555) 410-2200</p>
      <p class="contact__line">Pinefield &nbsp;(555) 306-4817</p>
      <p class="contact__line">Ridgeview</p>
      <p class="contact__line"><svg class="contact__icon" width="30" height="30" viewBox="0 0 30 30"><circle cx="15" cy="15" r="15" fill="#fff"/><path d="M10 8c1-1 2-1 3 0l1.5 2.5c.5 1 0 1.8-.8 2.3l-.7.5c.8 2 2.2 3.4 4.2 4.2l.5-.7c.5-.8 1.3-1.3 2.3-.8L22.5 17.5c1 1 1 2 0 3-3 3-8 0-10.5-2.5S7 11 10 8z" fill="var(--blue)"/></svg>(555) 230-1190</p>
    </div>
  </section>

  <!-- BACK -->
  <section class="card card--back">
    <svg class="shapes" viewBox="0 0 622 1398">
      <defs>
        <linearGradient id="gradEngine" x1="0" y1="0" x2="1" y2="1"><stop offset="0" stop-color="#2a2d31"/><stop offset="1" stop-color="#8a8f94"/></linearGradient>
        <linearGradient id="gradCabin" x1="0" y1="0" x2="0" y2="1"><stop offset="0" stop-color="#6c7278"/><stop offset="1" stop-color="#25282c"/></linearGradient>
        <linearGradient id="gradSeats" x1="0" y1="0" x2="1" y2="0"><stop offset="0" stop-color="#4b4f53"/><stop offset="1" stop-color="#a4a9ad"/></linearGradient>
      </defs>
      <rect x="0" y="0" width="622" height="330" fill="var(--white)"/>
      <polygon fill="var(--green)" points="0,330 140,330 140,500 0,745"/>
      <rect x="0" y="455" width="622" height="55" fill="var(--grey-band)"/>
      <polygon fill="var(--blue)" points="500,510 622,300 622,510"/>
      <polygon fill="var(--green)" points="500,1122 622,900 622,1398 560,1398"/>
      <polygon fill="var(--blue)" points="112,508 492,508 662,814 492,1120 112,1120 -58,814" stroke="var(--white)" stroke-width="8"/>
      <polygon fill="var(--green)" points="112,1136 492,1136 640,1398 -30,1398" stroke="var(--white)" stroke-width="8"/>

      <rect x="26" y="178" width="288" height="136" fill="none" stroke="var(--green)" stroke-width="2"/>
      <rect x="465" y="30" width="135" height="284" fill="none" stroke="var(--green)" stroke-width="2"/>
      <rect x="325" y="324" width="275" height="136" fill="none" stroke="var(--green)" stroke-width="2"/>

      <rect role="img" aria-label="Engine bay before cleaning, covered in leaves and dirt" x="30" y="35" width="252" height="127" fill="url(#gradEngine)"/>
      <rect role="img" aria-label="Engine bay after steam cleaning" x="30" y="182" width="252" height="128" fill="url(#gradEngine)"/>
      <rect role="img" aria-label="Dashboard and console before detailing" x="330" y="35" width="122" height="247" fill="url(#gradCabin)"/>
      <rect role="img" aria-label="Dashboard and console after detailing" x="470" y="35" width="125" height="247" fill="url(#gradCabin)"/>
      <rect role="img" aria-label="Front seats and floor before detailing" x="30" y="328" width="282" height="127" fill="url(#gradSeats)"/>
      <rect role="img" aria-label="Front seats and floor after detailing" x="330" y="328" width="265" height="127" fill="url(#gradSeats)"/>
      <polygon fill="var(--blue)" points="200,425 312,425 312,455 185,455"/>
      <polygon fill="var(--blue)" points="330,425 430,425 445,455 330,455"/>
    </svg>

    <div class="tag tag--v" style="left:282px;top:35px;width:30px;height:127px;">BEFORE</div>
    <div class="tag tag--v" style="left:282px;top:182px;width:30px;height:128px;">AFTER</div>
    <div class="tag" style="left:330px;top:282px;width:122px;height:28px;line-height:28px;">BEFORE</div>
    <div class="tag" style="left:470px;top:282px;width:125px;height:28px;line-height:28px;">AFTER</div>
    <div class="tag" style="left:200px;top:425px;width:112px;height:30px;line-height:30px;background:none;">BEFORE</div>
    <div class="tag" style="left:330px;top:425px;width:105px;height:30px;line-height:30px;background:none;">AFTER</div>

    <div class="abs prices">
      <p class="price">Premium Steam Washes<br>starting at $100 &amp; up</p>
      <p class="price">Full Steam Detailing<br>starting at $275 &amp; up</p>
      <p class="price">Paint Correction (multi-stage polishing)<br>starting at $650 &amp; up</p>
      <p class="price">Headlight Restoration - $110</p>
      <p class="price">Engine Steam Cleaning - $75</p>
    </div>

    <div class="abs slogan">
      <p class="slogan__script">Fall In Love With</p>
      <p class="slogan__bold">YOUR CAR AGAIN!</p>
    </div>

    <div class="abs cta">
      <p class="cta__note">Ceramic Coating-<br>Call or visit us for a Quote</p>
      <p class="cta__phone">(555) 230-1190</p>
      <p class="cta__web">www.brightmoorautocare.com</p>
    </div>
  </section>

</div>
</body>
</html>
```